Billboard

we want our Hop & Skip logo really big, we need this to stand out

Use a really bold font for the wording as it's on a billboard on the highway

Hop & Skip Logo
perhaps on left hand side really large then have a slanting line and a different colour background for the other side.

Wording BELOW-bold

TOUR NOW

hopandskip.edu.au

Use one image,
I have attached other designs we have been using for our campaign so a similar look would be great.
specs- 1224 W × 324 H px JPEG

Target Market(s)
families

Industry/Entity Type
childcare

Target Market(s)

families

Industry/Entity Type

childcare

Requirements
Must have
• bold font and big logo

```html
<!DOCTYPE html>
<html lang="en">
<head>
<meta charset="utf-8">
<title>Hop &amp; Skip – Tour Now Billboard</title>
<link rel="stylesheet" href="https://fonts.googleapis.com/css2?family=Titan+One&family=Archivo:wght@800&display=swap">
<style>
  :root {
    --sky-blue: #0a9fe0;
    --tomato: #e53f2e;
    --tomato-deep: #eb5a2c;
    --shadow-red: #b3301f;
    --lime: #dcdc00;
    --sun-yellow: #ffe400;
    --ink: #111111;
    --white: #ffffff;
    --page-light: #e4e4e4;
    --page-dark: #bdbdbd;
    --photo-sand: #c9a36b;
    --photo-teal: #3aa3b5;
  }
  * { box-sizing: border-box; margin: 0; padding: 0; }
  html, body {
    width: 1000px;
    height: 1200px;
    overflow: hidden;
  }
  body {
    background: linear-gradient(135deg, var(--page-dark), var(--page-light));
    position: relative;
  }
  .billboard {
    position: absolute;
    left: 50px;
    top: 481px;
    width: 900px;
    height: 238px;
    overflow: hidden;
    box-shadow: 0 10px 30px rgba(0, 0, 0, 0.35);
  }
  .billboard__shapes {
    position: absolute;
    inset: 0;
    width: 900px;
    height: 238px;
  }
  .brand {
    position: absolute;
    left: 0;
    top: 0;
    width: 250px;
    height: 238px;
    display: flex;
    flex-direction: column;
    align-items: center;
    justify-content: center;
    gap: 8px;
  }
  .brand__mark {
    width: 62px;
    height: 62px;
    border-radius: 50%;
    background: var(--sun-yellow);
  }
  .brand__name {
    font-family: "Titan One", sans-serif;
    color: var(--white);
    font-size: 38px;
    line-height: 1;
    text-align: center;
  }
  .headline {
    position: absolute;
    left: 250px;
    top: 22px;
    width: 420px;
    font-family: "Titan One", sans-serif;
    font-size: 98px;
    line-height: 0.98;
    text-align: center;
    color: #f4f4f4;
    text-shadow: 5px 5px 0 var(--shadow-red);
    letter-spacing: 1px;
  }
  .web-address {
    position: absolute;
    left: 615px;
    top: 190px;
    width: 285px;
    height: 48px;
    display: flex;
    align-items: center;
    justify-content: center;
    font-family: "Archivo", sans-serif;
    font-weight: 800;
    font-size: 15px;
    color: var(--ink);
  }
</style>
</head>
<body>
  <section class="billboard" aria-label="Hop &amp; Skip kindergarten billboard">
    <svg class="billboard__shapes" viewBox="0 0 900 238" aria-hidden="false">
      <defs>
        <linearGradient id="orangeFill" x1="0" y1="0" x2="1" y2="0">
          <stop offset="0" stop-color="var(--tomato)"/>
          <stop offset="1" stop-color="var(--tomato-deep)"/>
        </linearGradient>
        <linearGradient id="photoFill" x1="0" y1="0" x2="1" y2="1">
          <stop offset="0" stop-color="var(--photo-sand)"/>
          <stop offset="0.55" stop-color="#b98a55"/>
          <stop offset="1" stop-color="var(--photo-teal)"/>
        </linearGradient>
      </defs>
      <polygon class="panel-blue" points="0,0 272,0 232,238 0,238" fill="var(--sky-blue)"/>
      <polygon class="panel-orange" points="272,0 680,0 655,190 607,190 600,238 232,238" fill="url(#orangeFill)"/>
      <polygon class="panel-photo" points="680,0 900,0 900,190 655,190" fill="url(#photoFill)"
               role="img" aria-label="Photo of young children in sun hats playing with buckets and spades in a sandpit"/>
      <polygon class="panel-lime" points="607,190 900,190 900,238 600,238" fill="var(--lime)"/>
    </svg>

    <div class="brand">
      <span class="brand__mark" aria-hidden="true"></span>
      <p class="brand__name">Hop &amp;<br>Skip</p>
    </div>

    <h1 class="headline">TOUR<br>NOW</h1>

    <p class="web-address">www.HopAndSkip.edu.au</p>
  </section>
</body>
</html>
```